ThriftyShelfCraft (Custom Interior Trim work & Millwork Division)

ThriftyShelfCraft

Cabinetry & Interior Finish

We are a custom millwork shop and fabricate cabinets, mantles, media rooms, bookcases, cabinet doors, dovetail draws, etc.

Also specialize in interior finish work (crown molding, trim work, staircases, installing kitchens, etc.

In the 2nd image only use if you can get the light fixture out of the picture thank you

please visit my web sites to get more pics and ideas.

you can copy and paste text and pics

www.qwoodhausco.example

www.thriftyshelfcraft.example

I like the color green tied into this project somehow

Font styles to use
Serif

Colors
9bcb3c
ffffff
000000

Requirements
Must have
• needs to be professional
• look and feel correct
• I added colors I would like to see but please feel free to add and be creative
• thank you
• Phone number
• email
• pics
Nice to have
• A picture of myself
• go to my website and copy it
• www.thriftyshelfcraft.example
• If this comes out right I will award the winner a web page design for my company

```html
<!DOCTYPE html>
<html lang="en">
<head>
<meta charset="utf-8">
<title>ThriftyShelfCraft – Brochure Spreads</title>
<link rel="stylesheet" href="https://fonts.googleapis.com/css2?family=Oswald:wght@400;600&family=Open+Sans:wght@400;600;700&display=swap">
<style>
:root{
  --green:#9bcb3c;
  --green-dark:#7aa82a;
  --black:#000000;
  --ink:#2b2b2b;
  --white:#ffffff;
  --stage:#e9ebed;
  --grey:#f2f2f2;
}
*{box-sizing:border-box;margin:0;padding:0}
html,body{width:1200px;height:2404px;overflow:hidden}
body{background:var(--stage);font-family:"Open Sans",Arial,sans-serif;color:var(--ink);position:relative}
.spread{position:absolute;left:40px;width:1120px;height:740px;display:flex;box-shadow:0 6px 24px rgba(0,0,0,.18);background:var(--white)}
.spread-cover{top:40px}
.spread-inner-a{top:832px}
.spread-inner-b{top:1624px}
.page{position:relative;width:560px;height:740px;overflow:hidden;background:var(--white)}
.page+.page{border-left:1px solid #d6d6d6}
.photo{position:absolute;background:linear-gradient(135deg,#c9b79c,#8a6a48);border:2px solid var(--white)}
.photo.room{background:linear-gradient(135deg,#e7e3da,#a79d8c)}
.photo.house{background:linear-gradient(180deg,#b9d3ea 0%,#cfd6d9 45%,#8e9a7e 100%)}
.photo.dark{background:linear-gradient(135deg,#5b3e28,#2a1d14)}
.photo.white{background:linear-gradient(135deg,#fbfaf6,#cfcac0)}
.photo.portrait{background:linear-gradient(180deg,#ffffff 0%,#dfe7d0 60%,#9bcb3c 100%);border:none}
h2,h3,.display{font-family:"Oswald",Arial,sans-serif;font-weight:600;text-transform:uppercase;letter-spacing:.5px}
p{font-size:9.5px;line-height:1.45}
.tag{position:absolute;background:var(--green);color:var(--white);font-family:"Oswald",Arial,sans-serif;font-size:9px;padding:2px 6px;text-transform:uppercase}
.bar{background:var(--green);color:var(--white);font-size:11px;padding:4px 10px}
.subhead{color:var(--green-dark);font-family:"Oswald",Arial,sans-serif;font-size:11px;text-transform:uppercase;margin:8px 0 3px}
.bullet{display:flex;gap:6px;font-size:9.5px;line-height:1.5}
.bullet svg{flex:none;margin-top:3px}

/* cover back */
.back-strip{position:absolute;top:0;left:0;width:560px;height:56px;background:var(--green);color:var(--white);padding:8px 18px}
.back-strip h3{font-size:12px}
.back-strip p{font-size:8.5px;color:var(--white)}
.back-lower{position:absolute;left:0;top:392px;width:560px;height:348px;background:var(--green)}
.intro-panel{position:absolute;left:230px;top:392px;width:330px;height:348px;background:var(--black);color:var(--white);padding:34px 24px}
.intro-panel h2{color:var(--green);font-size:20px;text-transform:none;margin-bottom:10px}
.intro-panel p{color:#e6e6e6;font-size:10px;margin-bottom:8px}

/* cover front */
.front{background:var(--black)}
.brand{position:absolute;top:22px;left:0;width:560px;display:flex;flex-direction:column;align-items:center;gap:4px;color:var(--white)}
.brand-row{display:flex;align-items:center;gap:10px}
.brand-mark{width:18px;height:18px;background:var(--green)}
.brand-name{font-family:"Oswald",Arial,sans-serif;font-size:22px;font-weight:600;color:var(--white)}
.brand-sub{font-size:9px;color:var(--green);letter-spacing:1px;text-transform:uppercase}
.cover-grid{position:absolute;top:100px;left:20px;width:520px;height:400px;display:grid;grid-template-columns:repeat(3,1fr);grid-template-rows:repeat(3,1fr);gap:6px}
.cover-grid .photo{position:static}
.title-band{position:absolute;top:518px;left:0;width:560px;height:112px;background:var(--green);padding:16px 24px;color:var(--white)}
.title-band h1{font-family:"Oswald",Arial,sans-serif;font-weight:600;font-size:40px;line-height:1;letter-spacing:1px}
.title-band .lines{font-family:"Oswald",Arial,sans-serif;font-size:13px;margin-top:8px;line-height:1.4;text-transform:uppercase}
.contact{position:absolute;top:648px;left:24px;right:24px;color:var(--white);font-family:"Oswald",Arial,sans-serif}
.contact .row{display:flex;gap:18px;align-items:center;font-size:17px}
.contact .row span{display:flex;align-items:center;gap:6px}
.contact .url{color:var(--green);font-size:17px;margin-top:6px}

/* inner pages */
.about-box{position:absolute;left:0;top:0;width:250px;height:250px;background:var(--green);color:var(--white);padding:26px 20px}
.about-box h2{font-size:20px;margin-bottom:10px}
.about-box p{color:var(--white)}
.section{position:absolute;left:20px;right:20px}
.section h2{font-size:18px;color:var(--ink);display:flex;align-items:center;gap:8px;margin-bottom:6px}
.section h2 i{display:block;width:14px;height:14px;background:var(--green)}
.project{position:absolute}
.project .bar{margin-bottom:5px}
.project p{width:100%}
</style>
</head>
<body>

<!-- Spread 1: covers -->
<section class="spread spread-cover">
  <div class="page back">
    <div class="back-strip">
      <h3>Custom Built-In Cabinetry</h3>
      <p>Fine cabinets, bookcases and millwork made to fit your home and built to last for years.</p>
    </div>
    <div class="photo white" style="left:0;top:56px;width:150px;height:168px" role="img" aria-label="White built-in cabinets"></div>
    <div class="photo room" style="left:0;top:224px;width:150px;height:168px" role="img" aria-label="Kitchen island"></div>
    <div class="photo dark" style="left:150px;top:56px;width:230px;height:336px" role="img" aria-label="Media center with wood cabinetry"></div>
    <div class="photo room" style="left:380px;top:56px;width:180px;height:336px" role="img" aria-label="Green painted built-in shelves"></div>
    <div class="back-lower"></div>
    <div class="photo portrait" style="left:20px;top:420px;width:200px;height:300px" role="img" aria-label="Portrait of the owner"></div>
    <div class="intro-panel">
      <h2>Hi I'm Dan</h2>
      <p>We have been doing all sorts of quality carpentry work for many years. From built-in bookcases and mantles to full kitchens, every piece is made in our own shop.</p>
      <p>We take pride in our work and treat every home as if it were our own. Our goal is to give you lasting value at a fair price.</p>
      <p>If you have a project in mind, we would love to hear from you. Call or email for a free estimate.</p>
      <p style="color:var(--green)">Please call today for more information or visit our web site to see more.</p>
    </div>
  </div>

  <div class="page front">
    <div class="brand">
      <div class="brand-row"><span class="brand-mark"></span><span class="brand-name">ThriftyShelfCraft</span></div>
      <div class="brand-sub">Cabinetry &amp; Interior Finish</div>
    </div>
    <div class="cover-grid">
      <div class="photo white" role="img" aria-label="Painted cabinets"></div>
      <div class="photo room" role="img" aria-label="Built-in bookcase"></div>
      <div class="photo dark" role="img" aria-label="Dovetail drawers"></div>
      <div class="photo room" role="img" aria-label="Kitchen cabinetry"></div>
      <div class="photo white" role="img" aria-label="Wine rack cabinet"></div>
      <div class="photo" role="img" aria-label="Wood cabinet doors"></div>
      <div class="photo dark" role="img" aria-label="Round wood table top"></div>
      <div class="photo" role="img" aria-label="Red painted cabinet"></div>
      <div class="photo room" role="img" aria-label="Staircase trim"></div>
    </div>
    <div class="title-band">
      <h1>CUSTOM CABINATERY</h1>
      <div class="lines">Bookcases ■ Cabinets, Doors and Drawers<br>Media Centers ■ Mantles &amp; Special Projects</div>
    </div>
    <div class="contact">
      <div class="row">
        <span><svg width="16" height="16" viewBox="0 0 24 24"><path fill="#9bcb3c" d="M6.6 10.8a15 15 0 0 0 6.6 6.6l2.2-2.2c.3-.3.7-.4 1-.2 1.1.4 2.3.6 3.6.6.6 0 1 .4 1 1V20c0 .6-.4 1-1 1A17 17 0 0 1 3 4c0-.6.4-1 1-1h3.5c.6 0 1 .4 1 1 0 1.3.2 2.5.6 3.6.1.3 0 .7-.2 1z"/></svg>555-014-2280</span>
        <span><svg width="16" height="16" viewBox="0 0 24 24"><path fill="#9bcb3c" d="M3 5h18v14H3z"/><path fill="none" stroke="#000" stroke-width="1.6" d="M3 5l9 7 9-7"/></svg>dan@thriftyshelfcraft.example</span>
      </div>
      <div class="url">www.thriftyshelfcraft.example</div>
    </div>
  </div>
</section>

<!-- Spread 2: about, services, projects -->
<section class="spread spread-inner-a">
  <div class="page">
    <div class="about-box">
      <h2>About Us</h2>
      <p>Quincy Woodhaus Co. specializes in high quality home renovations, custom cabinetry and restoration. With exceptional skill and craftsmanship we help homeowners create the homes they imagine, on time and on budget.</p>
    </div>
    <div class="photo dark" style="left:250px;top:0;width:150px;height:130px" role="img" aria-label="Wood paneled room"></div>
    <div class="photo room" style="left:400px;top:0;width:160px;height:130px" role="img" aria-label="Kitchen with cabinets"></div>
    <div class="photo white" style="left:250px;top:130px;width:150px;height:120px" role="img" aria-label="White kitchen"></div>
    <div class="photo" style="left:400px;top:130px;width:160px;height:120px" role="img" aria-label="Ship wheel detail"></div>
    <div class="photo room" style="left:0;top:250px;width:140px;height:120px" role="img" aria-label="Dining room"></div>
    <div class="photo dark" style="left:140px;top:250px;width:140px;height:120px" role="img" aria-label="Library shelves"></div>
    <div class="photo white" style="left:280px;top:250px;width:140px;height:120px" role="img" aria-label="Bathroom vanity"></div>
    <div class="photo room" style="left:420px;top:250px;width:140px;height:120px" role="img" aria-label="Living room mantle"></div>
    <div class="section" style="top:390px">
      <h2><i></i>Services</h2>
      <div class="bar">New Construction, Renovation and Restoration</div>
      <p style="margin-top:5px">Quincy Woodhaus Co. specializes in high quality home renovations, antique and historic restoration and new home construction. With exceptional skill and craftsmanship we work closely with our clients to realize and create their vision, offering the broad skills and experience needed to turn ideas into finished rooms.</p>
      <div class="subhead">Project Management and Owner Representation</div>
      <p>As consultants on complex renovations, we represent owners in the management and oversight of the full building process. Services include:</p>
      <div style="margin-top:5px">
        <div class="bullet"><svg width="8" height="8"><rect width="8" height="8" fill="#9bcb3c"/></svg>Planning from project vision to final completion</div>
        <div class="bullet"><svg width="8" height="8"><rect width="8" height="8" fill="#9bcb3c"/></svg>Selection of architects, engineers, designers and contractors</div>
        <div class="bullet"><svg width="8" height="8"><rect width="8" height="8" fill="#9bcb3c"/></svg>Review of contract documents</div>
        <div class="bullet"><svg width="8" height="8"><rect width="8" height="8" fill="#9bcb3c"/></svg>Overseeing timely, successful project execution</div>
      </div>
    </div>
  </div>

  <div class="page">
    <div class="section" style="top:20px"><h2><i></i>Projects</h2></div>
    <div class="project" style="left:20px;top:52px;width:330px">
      <div class="bar">New Construction</div>
      <p>This before and after shows the original house was demolished and a new home designed to fit the neighborhood, built with care for every detail and finish.</p>
    </div>
    <div class="photo house" style="left:370px;top:52px;width:80px;height:66px" role="img" aria-label="House before"></div>
    <div class="photo house" style="left:460px;top:52px;width:80px;height:66px" role="img" aria-label="House after"></div>
    <span class="tag" style="left:370px;top:118px">Before</span><span class="tag" style="left:460px;top:118px">After</span>

    <div class="project" style="left:190px;top:160px;width:350px">
      <div class="bar">Additions and Renovations</div>
      <p>This growing family needed more space. We added a new master suite, a family room and a two car garage, and opened the kitchen to the rest of the home.</p>
    </div>
    <div class="photo house" style="left:20px;top:160px;width:75px;height:60px" role="img" aria-label="Addition exterior"></div>
    <div class="photo room" style="left:100px;top:160px;width:75px;height:60px" role="img" aria-label="Addition interior"></div>
    <div class="photo house" style="left:20px;top:226px;width:75px;height:60px" role="img" aria-label="Garage addition"></div>
    <div class="photo room" style="left:100px;top:226px;width:75px;height:60px" role="img" aria-label="New family room"></div>

    <div class="project" style="left:20px;top:320px;width:330px">
      <div class="bar">Linden Hall House</div>
      <p>This is a classic New England Victorian home in need of exterior restoration. The original details were carefully repaired, siding and trim were replaced where needed and the porch was rebuilt to match.</p>
    </div>
    <div class="photo house" style="left:370px;top:320px;width:80px;height:66px" role="img" aria-label="Victorian house before"></div>
    <div class="photo house" style="left:460px;top:320px;width:80px;height:66px" role="img" aria-label="Victorian house after"></div>
    <span class="tag" style="left:370px;top:386px">Before</span><span class="tag" style="left:460px;top:386px">After</span>

    <div class="project" style="left:190px;top:450px;width:350px">
      <div class="bar">Brookline Apartment</div>
      <p>A complete gut renovation of a city apartment. We rebuilt the kitchen and bath, refinished the floors and added custom built-ins to make the most of every square foot.</p>
    </div>
    <div class="photo room" style="left:20px;top:450px;width:75px;height:60px" role="img" aria-label="Apartment kitchen"></div>
    <div class="photo white" style="left:100px;top:450px;width:75px;height:60px" role="img" aria-label="Apartment bath"></div>
    <div class="photo room" style="left:20px;top:516px;width:75px;height:60px" role="img" aria-label="Apartment living room"></div>
    <div class="photo dark" style="left:100px;top:516px;width:75px;height:60px" role="img" aria-label="Apartment built-ins"></div>
    <div style="position:absolute;left:0;bottom:0;width:560px;height:30px;background:var(--green)"></div>
  </div>
</section>

<!-- Spread 3: more projects -->
<section class="spread spread-inner-b">
  <div class="page">
    <div class="project" style="left:20px;top:24px;width:330px">
      <div class="bar">Custom Renovation</div>
      <p>An inviting brick home in need of updating. We redesigned the layout, rebuilt the stair and added new trim throughout while keeping the character of the house intact.</p>
    </div>
    <div class="photo room" style="left:370px;top:24px;width:80px;height:66px" role="img" aria-label="Stair before"></div>
    <div class="photo white" style="left:460px;top:24px;width:80px;height:66px" role="img" aria-label="Stair after"></div>

    <div class="section" style="top:130px"><div class="bar">Antique and Historic Restorations</div></div>
    <div class="photo house" style="left:20px;top:162px;width:160px;height:110px" role="img" aria-label="Historic house"></div>
    <div class="project" style="left:195px;top:162px;width:345px">
      <div class="subhead" style="margin-top:0">Maple Row House</div>
      <p>This colonial farmhouse had undergone many changes over the years. We restored its original layout, repaired the timber frame, replaced failing windows and brought back period trim, floors and doors so it reads once more as it did when first built.</p>
    </div>
    <span class="tag" style="left:20px;top:272px">Before</span>
    <div class="photo house" style="left:20px;top:300px;width:160px;height:110px" role="img" aria-label="Restored historic house"></div>
    <span class="tag" style="left:20px;top:410px">After</span>
    <div class="photo house" style="left:200px;top:300px;width:160px;height:110px" role="img" aria-label="Estate before"></div>
    <div class="photo house" style="left:380px;top:300px;width:160px;height:110px" role="img" aria-label="Estate after"></div>
    <span class="tag" style="left:200px;top:410px">Before</span><span class="tag" style="left:380px;top:410px">After</span>

    <div class="project" style="left:20px;top:450px;width:520px">
      <div class="subhead">Harbor View Estate</div>
      <p>The Harbor View home is a unique historic property. Working with the owners, our team restored the exterior, rebuilt the porches and brought the interior up to date with new systems.</p>
      <p style="margin-top:6px">The project was designed around a new kitchen, updated baths and new landscaping that ties the home to its setting. Every part of the work respected the style and history of the house.</p>
    </div>
    <div class="photo room" style="left:20px;top:600px;width:120px;height:90px" role="img" aria-label="Kitchen before"></div>
    <div class="photo white" style="left:150px;top:600px;width:120px;height:90px" role="img" aria-label="Kitchen after"></div>
    <div class="photo room" style="left:290px;top:600px;width:120px;height:90px" role="img" aria-label="Dining before"></div>
    <div class="photo dark" style="left:420px;top:600px;width:120px;height:90px" role="img" aria-label="Dining after"></div>
    <span class="tag" style="left:20px;top:690px">Before</span><span class="tag" style="left:150px;top:690px">After</span>
    <span class="tag" style="left:290px;top:690px">Before</span><span class="tag" style="left:420px;top:690px">After</span>
  </div>

  <div class="page">
    <div class="project" style="left:20px;top:24px;width:520px">
      <div class="bar">Kitchens, Laundry and Baths</div>
    </div>
    <div class="project" style="left:20px;top:56px;width:250px">
      <div class="subhead">Kitchens</div>
      <p>A place to gather, cook and share. From simple updates to complete rebuilds, we create kitchens that work as well as they look.</p>
    </div>
    <div class="photo white" style="left:290px;top:60px;width:120px;height:90px" role="img" aria-label="White kitchen"></div>
    <div class="photo room" style="left:420px;top:60px;width:120px;height:90px" role="img" aria-label="Kitchen island"></div>
    <div class="project" style="left:290px;top:170px;width:250px">
      <div class="subhead">Laundry and Bath</div>
      <p>Your bath can be a calm retreat. We build vanities, tile showers and tidy laundry rooms with custom storage.</p>
    </div>
    <div class="photo white" style="left:20px;top:176px;width:120px;height:90px" role="img" aria-label="Bathroom"></div>
    <div class="photo room" style="left:150px;top:176px;width:120px;height:90px" role="img" aria-label="Laundry room"></div>

    <div class="project" style="left:20px;top:300px;width:520px">
      <div class="bar">Specialty Projects &amp; Custom Carpentry</div>
    </div>
    <div class="project" style="left:20px;top:332px;width:250px">
      <div class="subhead">Fleet Street, Boston</div>
      <p>We designed and built custom cabinetry, paneled walls and a library with rolling ladder for this city home, using cherry and walnut throughout.</p>
    </div>
    <div class="photo dark" style="left:290px;top:336px;width:120px;height:90px" role="img" aria-label="Library with shelves"></div>
    <div class="photo" style="left:420px;top:336px;width:120px;height:90px" role="img" aria-label="Paneled wall"></div>

    <div class="project" style="left:290px;top:450px;width:250px">
      <div class="subhead">Tree House in the Hills</div>
      <p>This tree house was built for two young brothers, with a deck, rope bridge and a small loft. The design fits the trees without harming them.</p>
      <p style="margin-top:6px">The home was fully updated inside as well, with a new stair, built-in benches and trim that ties the rooms together.</p>
    </div>
    <div class="photo house" style="left:20px;top:456px;width:120px;height:100px" role="img" aria-label="Tree house"></div>
    <div class="photo house" style="left:150px;top:456px;width:120px;height:100px" role="img" aria-label="Tree house deck"></div>
    <div class="photo room" style="left:20px;top:566px;width:250px;height:100px" role="img" aria-label="Interior stair"></div>
    <div style="position:absolute;left:0;bottom:0;width:560px;height:30px;background:var(--green)"></div>
  </div>
</section>

</body>
</html>
```